Prominent Law Firm Needs a New Stationary Design

We need new stationary design to go with our new logo and rustic offices.
Things we need on the letterhead:
logo (see attached file), would also like the Multi-Million Dollar Logo (attached) somewhere on the stationary,
3182 North Pellam Street
Tulsa, Oklahoma 74105
(918) 555-0142 Tel ★ (918) 555-0187 Fax
www.TFWLAW.example

We also need the names of the 4 partners:
Dennis W. Hollister
Walter E. Hollister
Kevin M. Abernathy
Brian D. Whitcombe

And the other staff:
Janet K. Bowden
Tendai K. Chikwanda
Howard Pimsley

Lorraine F. Tuttle, RN

Of Counsel:
Prescott D. Hollister

```html
<!DOCTYPE html>
<html lang="en">
<head>
<meta charset="utf-8">
<title>Hollister Hollister Abernathy — Business Card</title>
<link rel="stylesheet" href="https://fonts.googleapis.com/css2?family=Domine:wght@400;700&display=swap">
<style>
  :root {
    --backdrop: #8b8b8b;
    --card: #2a2a2a;
    --silver: #d4d4d4;
    --silver-soft: #b9b9b9;
    --rule: #a9a9a9;
  }
  * { box-sizing: border-box; margin: 0; padding: 0; }
  html, body { width: 1200px; height: 900px; overflow: hidden; }
  body {
    background: var(--backdrop);
    font-family: "Domine", Georgia, serif;
    color: var(--silver);
    position: relative;
  }
  .card {
    position: absolute;
    left: 321px;
    width: 522px;
    height: 289px;
    background: var(--card);
  }
  .card--front { top: 119px; }
  .card--back { top: 472px; }
  .card__frame {
    position: absolute;
    inset: 16px 17px 16px 17px;
    border: 1px solid var(--silver-soft);
  }
  .centered {
    position: absolute;
    left: 0;
    right: 0;
    text-align: center;
  }
  .firm-mark {
    top: 112px;
    font-weight: 400;
    font-size: 22px;
    letter-spacing: 2px;
    text-transform: uppercase;
  }
  .firm-mark__dot {
    position: absolute;
    left: 252px;
    top: 158px;
    width: 18px;
    height: 18px;
    border-radius: 50%;
    background: var(--silver);
  }
  .firm-name {
    top: 52px;
    font-size: 17px;
    letter-spacing: 2px;
    text-transform: uppercase;
  }
  .person-name {
    top: 116px;
    font-weight: 700;
    font-size: 23px;
  }
  .person-title {
    top: 151px;
    font-size: 18px;
    color: var(--silver-soft);
  }
  .divider {
    position: absolute;
    left: 100px;
    top: 193px;
  }
  .contact-line {
    top: 211px;
    font-size: 14px;
    color: var(--silver-soft);
    word-spacing: 1px;
  }
  .contact-line span + span { margin-left: 24px; }
  .address-line {
    top: 243px;
    font-size: 13px;
    color: var(--silver-soft);
  }
</style>
</head>
<body>
  <section class="card card--front" aria-label="Card front">
    <div class="card__frame"></div>
    <p class="centered firm-mark">Hollister Hollister Abernathy</p>
    <div class="firm-mark__dot"></div>
  </section>

  <section class="card card--back" aria-label="Card back">
    <div class="card__frame"></div>
    <p class="centered firm-name">Hollister Hollister Abernathy</p>
    <h1 class="centered person-name">Dennis W. Hollister</h1>
    <p class="centered person-title">Chairman &amp; CEO</p>
    <svg class="divider" width="322" height="8" viewBox="0 0 322 8" aria-hidden="true">
      <line x1="0" y1="4" x2="322" y2="4" stroke="#a9a9a9" stroke-width="1"/>
      <circle cx="161" cy="4" r="3.5" fill="#c4c4c4"/>
    </svg>
    <p class="centered contact-line">
      <span>dennis@tfwlaw.example</span><span>(877) 555.0163</span><span>www.tfwlaw.example</span>
    </p>
    <p class="centered address-line">3182 North Pellam Street, Tulsa, OK 74105</p>
  </section>
</body>
</html>
```